I need a business card for a new small local scaffolding company. I supply and erect all types of scaffolding for any access need. I thought I could put a safety hat on the Q in NQ to emphasize the 'safe' in KORVELTA. Just a thought.

Industry/Entity Type

Safety

Contact Information for Business Card

KORVELTA NQ , Rob Tenwick , All scaffold & access solutions , Hire , Sales , Transport ,email korveltanq@brisomail.net , 0438710536, fully accredited , abn 47290318854

```html
<!DOCTYPE html>
<html lang="en">
<head>
<meta charset="utf-8">
<title>KORVELTA NQ — Business Card</title>
<link rel="stylesheet" href="https://fonts.googleapis.com/css2?family=Roboto+Condensed:wght@700&family=Roboto:wght@700&display=swap">
<style>
  :root {
    --page-bg: #f2f2f2;
    --card-white: #ffffff;
    --scaffold-grey: #e4e6e8;
    --brand-red: #d4151b;
    --brand-red-dark: #a80f13;
    --ink-black: #111111;
    --panel-black: #1a1a1a;
    --panel-black-deep: #0b0b0b;
    --steel: #b9bcbf;
    --text-light: #e6e6e6;
    --text-muted: #8a8a8a;
  }
  * { margin: 0; padding: 0; box-sizing: border-box; }
  html, body {
    width: 1200px;
    height: 900px;
    overflow: hidden;
    background: var(--page-bg);
  }
  .canvas {
    position: relative;
    width: 1200px;
    height: 900px;
  }
  .business-card {
    position: absolute;
    left: 100px;
    top: 165px;
    width: 1000px;
    height: 570px;
    border-radius: 44px;
    overflow: hidden;
    background: var(--card-white);
    box-shadow: 0 20px 40px rgba(0,0,0,0.18);
  }
  .card-top {
    position: absolute;
    inset: 0 0 auto 0;
    height: 310px;
  }
  .scaffold-backdrop {
    position: absolute;
    inset: 0;
    background: linear-gradient(180deg, var(--scaffold-grey) 0%, #f7f7f7 55%, #e9eaeb 100%);
  }
  .accreditation {
    position: absolute;
    top: 62px;
    width: 100%;
    text-align: center;
    font-family: "Roboto", Arial, sans-serif;
    font-weight: 700;
    font-size: 20px;
    letter-spacing: 3px;
    color: var(--brand-red);
  }
  .brand-lockup {
    position: absolute;
    top: 118px;
    width: 100%;
    display: flex;
    justify-content: center;
    align-items: center;
    gap: 22px;
  }
  .brand-name {
    font-family: "Roboto Condensed", "Arial Narrow", sans-serif;
    font-weight: 700;
    font-size: 118px;
    line-height: 1;
    letter-spacing: 2px;
    color: var(--brand-red);
  }
  .brand-dot {
    width: 34px;
    height: 34px;
    border-radius: 50%;
    background: var(--brand-red);
  }
  .service-band {
    position: absolute;
    top: 300px;
    left: 0;
    width: 100%;
    height: 40px;
    background: var(--brand-red);
    border-bottom: 4px solid var(--steel);
    display: flex;
    align-items: center;
    justify-content: center;
    font-family: "Roboto", Arial, sans-serif;
    font-weight: 700;
    font-size: 21px;
    letter-spacing: 3.5px;
    color: var(--ink-black);
  }
  .card-bottom {
    position: absolute;
    top: 340px;
    left: 0;
    width: 100%;
    height: 230px;
    background: radial-gradient(ellipse at 50% 30%, var(--panel-black) 0%, var(--panel-black-deep) 100%);
    text-align: center;
  }
  .contact-name {
    margin-top: 26px;
    font-family: "Roboto Condensed", "Arial Narrow", sans-serif;
    font-weight: 700;
    font-size: 42px;
    color: var(--brand-red);
  }
  .contact-phone,
  .contact-email {
    font-family: "Roboto", Arial, sans-serif;
    font-weight: 700;
    color: var(--text-light);
  }
  .contact-phone {
    margin-top: 22px;
    font-size: 30px;
    letter-spacing: 1px;
  }
  .contact-email {
    margin-top: 2px;
    font-size: 31px;
  }
  .contact-abn {
    margin-top: 2px;
    font-family: "Roboto", Arial, sans-serif;
    font-weight: 700;
    font-size: 18px;
    color: var(--text-muted);
  }
</style>
</head>
<body>
<div class="canvas">
  <div class="business-card">
    <div class="card-top">
      <div class="scaffold-backdrop" role="img" aria-label="Faint scaffolding frame structure in the background"></div>
      <p class="accreditation">FULLY ACCREDITED</p>
      <div class="brand-lockup">
        <span class="brand-name">KORVELTA NQ</span>
        <span class="brand-dot"></span>
      </div>
    </div>
    <div class="service-band">ALL SCAFFOLD &amp; ACCESS SOLUTIONS , HIRE , SALES , TRANSPORT</div>
    <div class="card-bottom">
      <p class="contact-name">Rob Tenwick</p>
      <p class="contact-phone">0438710536</p>
      <p class="contact-email">korveltanq@brisomail.net</p>
      <p class="contact-abn">abn 47290318854</p>
    </div>
  </div>
</div>
</body>
</html>
```